Brivosta Films
Creative and Dynamic Independent Films
Professional
Marcus Tollen
OWNER/PRODUCER/
47 Haldon Ave
Marlow Falls PA 18790
Marcus@BrivostaFilms.com
www.BrivostaFilms.com
Bold,Regal,Elegant
Logo File.

```html
<!DOCTYPE html>
<html lang="en">
<head>
<meta charset="utf-8">
<title>Brivosta Films — Stationery Set</title>
<link href="https://fonts.googleapis.com/css2?family=Cinzel:wght@700&family=Open+Sans:wght@400;600&display=swap" rel="stylesheet">
<style>
  :root{
    --stage:#e9e6e1;
    --paper:#ffffff;
    --navy:#0c2238;
    --blue:#2b6f9c;
    --sky:#5fa3cf;
    --gold:#d9a23a;
    --gold-light:#f2c867;
    --ink:#2b3440;
    --muted:#8a939c;
    --rule:#c9d0d6;
    --ghost:rgba(43,111,156,.08);
  }
  *{box-sizing:border-box;margin:0;padding:0}
  html,body{width:1200px;height:538px;overflow:hidden}
  body{background:var(--stage);font-family:"Open Sans",sans-serif;color:var(--ink);position:relative}
  .item{position:absolute}
  .item-label{position:absolute;top:-12px;left:0;right:0;text-align:center;font-size:7px;font-weight:600;color:var(--muted);letter-spacing:.04em}
  .sheet{background:var(--paper);box-shadow:0 2px 6px rgba(0,0,0,.18);overflow:hidden}
  .swoosh{position:absolute;top:0;right:0;height:100%;width:100%;pointer-events:none}
  .brand{font-family:"Cinzel",serif;font-weight:700;color:var(--navy);text-align:center;letter-spacing:.06em;display:flex;align-items:center;justify-content:center;gap:5px}
  .brand .dot{width:8px;height:8px;border-radius:50%;background:var(--blue);flex:none}
  .ghost{position:absolute;left:0;right:0;display:flex;flex-direction:column;align-items:center;gap:10px}
  .ghost .ring{width:120px;height:120px;border-radius:50%;background:var(--ghost)}
  .ghost .ghost-name{font-family:"Cinzel",serif;font-weight:700;font-size:26px;color:var(--ghost);letter-spacing:.08em}
  .footer-line{position:absolute;left:0;right:0;text-align:center;font-size:5px;color:var(--muted)}

  /* fax */
  .fax{left:19px;top:24px;width:281px;height:372px}
  .fax .brand{position:absolute;top:14px;left:0;right:0;font-size:11px}
  .fax-title{position:absolute;top:42px;right:26px;font-family:"Cinzel",serif;font-weight:700;font-size:10px;color:var(--navy)}
  .fax-table{position:absolute;top:56px;left:14px;width:240px;border-collapse:collapse;font-size:6px}
  .fax-table td{border:1px solid var(--rule);height:15px;padding:0 4px}
  .fax-table td.key{width:30px;font-weight:600;color:var(--navy)}
  .fax-checks{position:absolute;top:132px;left:14px;width:240px;display:flex;justify-content:space-between;font-size:5.5px}
  .fax-checks span::before{content:"";display:inline-block;width:5px;height:5px;border:1px solid var(--muted);margin-right:3px;vertical-align:middle}
  .fax .ghost{top:175px}

  /* letterheads */
  .letterhead{top:24px;width:265px;height:372px}
  .lh-a{left:305px}
  .lh-b{left:583px}
  .letterhead .brand{position:absolute;top:14px;left:0;right:0;font-size:11px}
  .lh-contact{position:absolute;top:14px;left:14px;font-size:5px;line-height:1.5;color:var(--muted)}
  .letterhead .ghost{top:120px}

  /* cards */
  .card{top:24px;width:156px;height:67px}
  .card-front{left:864px}
  .card-back{left:1027px}
  .card-front .brand{position:absolute;top:10px;right:28px;font-size:8px}
  .card-details{position:absolute;left:10px;top:26px;font-size:5px;line-height:1.5}
  .card-details strong{color:var(--navy);font-size:6px}
  .card-back .brand{position:absolute;top:24px;left:0;right:0;font-size:10px}

  /* compliment */
  .compliment{left:864px;top:110px;width:319px;height:118px}
  .compliment .brand{position:absolute;top:30px;left:0;right:0;font-size:14px}
  .compliment-tag{position:absolute;top:52px;left:0;right:0;text-align:center;font-size:6px;color:var(--muted);letter-spacing:.1em}

  /* envelopes */
  .envelope{left:864px;width:319px;height:78px}
  .env-white{top:290px}
  .env-gold{top:330px}
  .envelope svg{position:absolute;inset:0;width:100%;height:100%}
  .envelope .brand{position:absolute;left:0;right:0;font-size:8px}
  .env-white .brand{top:22px;color:#fff}
  .env-gold .brand{top:26px}
</style>
</head>
<body>

<svg width="0" height="0" style="position:absolute">
  <defs>
    <linearGradient id="swooshFill" x1="0" y1="0" x2="1" y2="1">
      <stop offset="0" stop-color="#0c2238"/>
      <stop offset=".55" stop-color="#2b6f9c"/>
      <stop offset="1" stop-color="#5fa3cf"/>
    </linearGradient>
    <linearGradient id="goldFill" x1="0" y1="0" x2="0" y2="1">
      <stop offset="0" stop-color="#f2c867"/>
      <stop offset="1" stop-color="#c98d26"/>
    </linearGradient>
  </defs>
</svg>

<!-- Fax sheet -->
<section class="item sheet fax">
  <div class="item-label">Fax Sheet</div>
  <svg class="swoosh" viewBox="0 0 100 100" preserveAspectRatio="none"><path d="M100 0 L93 0 Q99 50 93 100 L100 100 Z" fill="url(#swooshFill)"/></svg>
  <div class="brand"><span class="dot"></span>BRIVOSTA FILMS</div>
  <div class="fax-title">FAX</div>
  <table class="fax-table">
    <tr><td class="key">To:</td><td></td><td class="key">From:</td><td></td></tr>
    <tr><td class="key">Fax:</td><td></td><td class="key">Pages:</td><td></td></tr>
    <tr><td class="key">Phone:</td><td></td><td class="key">Date:</td><td></td></tr>
    <tr><td class="key">Re:</td><td></td><td class="key">CC:</td><td></td></tr>
  </table>
  <div class="fax-checks">
    <span>Urgent</span><span>For Review</span><span>Please Comment</span><span>Please Reply</span><span>Please Recycle</span>
  </div>
  <div class="ghost"><div class="ring"></div><div class="ghost-name">BRIVOSTA</div></div>
  <div class="footer-line" style="bottom:12px">47 Haldon Ave · Marlow Falls PA 18790 · (570) 555-0142 · www.BrivostaFilms.com</div>
</section>

<!-- Letterhead A -->
<section class="item sheet letterhead lh-a">
  <div class="item-label">Letterhead</div>
  <svg class="swoosh" viewBox="0 0 100 100" preserveAspectRatio="none"><path d="M100 0 L93 0 Q99 50 93 100 L100 100 Z" fill="url(#swooshFill)"/></svg>
  <div class="lh-contact">Marcus Tollen<br>47 Haldon Ave<br>Marlow Falls PA 18790<br>(570) 555-0142</div>
  <div class="brand" style="top:40px"><span class="dot"></span>BRIVOSTA FILMS</div>
  <div class="ghost"><div class="ring"></div><div class="ghost-name">BRIVOSTA</div></div>
</section>

<!-- Letterhead B -->
<section class="item sheet letterhead lh-b">
  <div class="item-label">Letterhead</div>
  <svg class="swoosh" viewBox="0 0 100 100" preserveAspectRatio="none"><path d="M100 0 L93 0 Q99 50 93 100 L100 100 Z" fill="url(#swooshFill)"/></svg>
  <div class="brand"><span class="dot"></span>BRIVOSTA FILMS</div>
  <div class="ghost"><div class="ring"></div><div class="ghost-name">BRIVOSTA</div></div>
  <div class="footer-line" style="bottom:14px">47 Haldon Ave · Marlow Falls PA 18790<br>Marcus@BrivostaFilms.com · www.BrivostaFilms.com</div>
</section>

<!-- Business card front -->
<section class="item sheet card card-front">
  <div class="item-label">Business Card Front</div>
  <svg class="swoosh" viewBox="0 0 100 100" preserveAspectRatio="none"><path d="M100 0 L86 0 Q96 50 86 100 L100 100 Z" fill="url(#swooshFill)"/></svg>
  <div class="brand"><span class="dot"></span>BRIVOSTA</div>
  <div class="card-details"><strong>Marcus Tollen</strong><br>Owner / Producer<br>47 Haldon Ave, Marlow Falls PA 18790<br>Marcus@BrivostaFilms.com</div>
</section>

<!-- Business card back -->
<section class="item sheet card card-back">
  <div class="item-label">Business Card Back</div>
  <svg class="swoosh" viewBox="0 0 100 100" preserveAspectRatio="none"><path d="M100 0 L86 0 Q96 50 86 100 L100 100 Z" fill="url(#swooshFill)"/></svg>
  <div class="brand"><span class="dot"></span>BRIVOSTA</div>
</section>

<!-- Compliment card -->
<section class="item sheet compliment">
  <div class="item-label">Compliment Card</div>
  <svg class="swoosh" viewBox="0 0 100 100" preserveAspectRatio="none"><path d="M100 0 L94 0 Q99 50 94 100 L100 100 Z" fill="url(#swooshFill)"/></svg>
  <div class="brand"><span class="dot"></span>BRIVOSTA FILMS</div>
  <div class="compliment-tag">CREATIVE AND DYNAMIC INDEPENDENT FILMS</div>
</section>

<!-- Envelope white -->
<section class="item envelope env-white">
  <div class="item-label">Envelope Back</div>
  <svg viewBox="0 0 319 78" preserveAspectRatio="none">
    <rect width="319" height="78" fill="#fff"/>
    <path d="M0 0 H319 L180 50 Q160 58 140 50 Z" fill="url(#swooshFill)"/>
  </svg>
  <div class="brand"><span class="dot" style="background:#fff"></span>BRIVOSTA</div>
</section>

<!-- Envelope gold -->
<section class="item envelope env-gold">
  <svg viewBox="0 0 319 78" preserveAspectRatio="none">
    <rect width="319" height="78" fill="url(#goldFill)"/>
    <path d="M0 0 H319 L180 50 Q160 58 140 50 Z" fill="#fff" opacity=".9"/>
  </svg>
  <div class="brand"><span class="dot"></span>BRIVOSTA</div>
</section>

</body>
</html>
```